Book cover required for new book business book (Heron Glide SEO for Managed Service Providers)

We are finalizing publishing dates for our latest business book. The audience this book is targetting is IT business owners. Demographic age 30-50 years of age, male, middle class. The title of the book is Heron Glide SEO for managed service providers. The author name is Dewan Corby. The book goes into details about how to improve SEO for IT businesses. The premise of the book is if a bear attacked a crowd of people, and you were in that crowd, you'd only have to be 1% faster to outrun the bear. The same is true for your IT Businesses website. You only have to put in 1% more effort into your SEO to be on page one of Zentrik.
We have been using a working draft image whilst the book has been in preproduction. I am unsure if this working image is licensed. Please find attached.

```html
<!DOCTYPE html>
<html lang="en">
<head>
<meta charset="utf-8">
<title>Heron Glide SEO for Managed Service Providers — Book Cover</title>
<link rel="stylesheet" href="https://fonts.googleapis.com/css2?family=Cinzel:wght@400;500;600&display=swap">
<style>
  :root {
    --backdrop: #e4eaee;
    --paper: #ffffff;
    --title-blue: #0b57a6;
    --title-navy: #15304f;
    --claw-dark: #3a3a3c;
    --claw-light: #cfd1d3;
  }
  * { margin: 0; padding: 0; box-sizing: border-box; }
  html, body {
    width: 1200px;
    height: 1200px;
    overflow: hidden;
    background: var(--backdrop);
  }
  .canvas {
    position: relative;
    width: 1200px;
    height: 1200px;
  }
  .book-cover {
    position: absolute;
    left: 223px;
    top: 35px;
    width: 754px;
    height: 1130px;
    background: var(--paper);
    overflow: hidden;
    font-family: "Cinzel", "Times New Roman", serif;
  }
  .claw-marks {
    position: absolute;
    right: 0;
    top: 0;
    width: 400px;
    height: 410px;
    background: linear-gradient(225deg, var(--claw-dark) 0%, #6b6c6e 40%, var(--claw-light) 75%, rgba(255,255,255,0) 100%);
    clip-path: polygon(40% 0, 100% 0, 100% 55%, 45% 100%, 0 85%);
  }
  .title-line {
    position: absolute;
    left: 0;
    width: 100%;
    text-align: center;
    line-height: 1;
    white-space: nowrap;
  }
  .title-heron {
    top: 192px;
    font-size: 150px;
    font-weight: 500;
    color: var(--title-blue);
    letter-spacing: 2px;
    padding-left: 70px;
  }
  .title-glide {
    top: 350px;
    font-size: 112px;
    font-weight: 400;
    color: var(--title-navy);
    padding-left: 70px;
  }
  .title-seo {
    top: 462px;
    font-size: 246px;
    font-weight: 500;
    color: var(--title-blue);
    padding-left: 70px;
  }
  .subtitle {
    position: absolute;
    left: 0;
    top: 696px;
    width: 100%;
    padding-left: 70px;
    text-align: center;
    font-size: 46px;
    line-height: 63px;
    font-weight: 400;
    color: var(--title-navy);
  }
  .author {
    position: absolute;
    left: 0;
    top: 1012px;
    width: 100%;
    padding-left: 70px;
    text-align: center;
    font-size: 68px;
    font-weight: 500;
    color: var(--title-navy);
    letter-spacing: 1px;
  }
</style>
</head>
<body>
  <main class="canvas">
    <section class="book-cover">
      <div class="claw-marks" role="img" aria-label="Torn claw-scratch marks ripping through the top right corner of the cover"></div>
      <h1>
        <span class="title-line title-heron">HERON</span>
        <span class="title-line title-glide">GLIDE</span>
        <span class="title-line title-seo">SEO</span>
      </h1>
      <p class="subtitle">FOR MANAGED<br>SERVICE PROVIDERS</p>
      <p class="author">Dewan Corby</p>
    </section>
  </main>
</body>
</html>
```